Sassy Funky Web Design Project

NOTE: PAYMENT IS GUARANTEED for this project :)

++++++++++++++++++

I meant to share with you my mission for Caring Summit:

To inspire nurses to take action that impacts change in their lives, their organizations, or even the world.

Values:
I – Integrity
M – Mentoring / Motivation
P – Passion for excellence
A – Accountability
C – Competence / knowledge/ achievement
T – Transformation – positive change

++++++++++++++++++

This is a Membership site so will need to show 'Members Login' etc.

Please make sure you use SUPER HIGH QUALITY PHOTOGRAPHY / IMAGES :)

This is a WORDPRESS site for my client - here's some questions I asked her with her answers:

1. Why do you want a website (or have your current site redesigned)?

I want a website to generate income, and residual income, promote quality education material to professionals that is not the same on-line programs point and click to answer questions. I want an interactive way to make a impact in nursing hence CaringSUMMIT.

2. What’s your business/organization all about?

My parent company is Verity Brook Partners, LLC. I started it in 2001 and I provide consultative services to the legal and medical professionals. Mostly legal professionals; attorneys, and offer expert witness testimony. I also present full-day seminars regarding legal aspects of healthcare for nurses and hospital executive leaders. I am always promoting the professionalism in nursing where ever I can.

3. What sets your business apart from your competition?

What I will offer is instant access to quality and reliable clinical information and reliable business support for legal nurse consultants. I have not found another website that offers videos of clinical skills that nurses can watch over and over again without paying a lot of money for. Most of the information for nurses is through online learning read a packet, answer questions, and hopefully, maybe, they learned something. One of the reasons why my seminars are so well attended is they are interactive, and I use real examples to act out scenarios. I want nurses to be able to access short 7-10 minute video/podcasts that will show them how things are done and not just reading about it. Assessment skills will be performed on my family members in a clinic setting to create a realistic view. I want these to be somehow interactive if possible to reinforce the learning. Maybe you have some ideas on that.

For the legal nurse consultants. The programs are driving the “certification” outcome. When the nurses complete these programs, they have no experience and therefore are not able to recover their investment. I want to provide for them the same type of visual education support as the clinical nurses. These two audiences do not have to be mutually exclusive because they do tend to overlap in the real world.

I provide personal mentoring for novice legal nurse consultants in one week programs to support the application need in the LNC community. These weeks are valuable to the novice LNC trying to get started.

4. What problems does your business solve?

Application of concepts which is where I came up with Verity Brook Partners. I also have a tag with CaringSUMMIT I have used: Education, training, application. I put the theory into practice. I translate the pages to the living people.

5. Who are your prospective customers or visitors?

Customers:
Nurses, Advanced Practice Nurses, Legal Nurse Consultants, Attorneys for the clinical/medical information, Universities that offer nursing programs,
Nursing students (I really want to pursue this niche, perhaps a discount for enrolled students???)

Visitors:
Hospital Chief Nursing Officers, Attorneys, Long Term Care Administrators, Faculty of Nursing programs.

6. What do you NOT want on your website?

A flat appearing, boxy, traditional site. I want the nurses to be able to navigate through without much effort, remember many are technologically challenged….
NOooo cartoons… not too many stock photos, I would rather take real images if at all possible to keep the site “alive and real”.

What do you like?

QRV.tv: the listing of videos is going to be important in my site because I will be making clinical example videos and interview videos that can be viewed over and over again by the Platinum members. I plan to have a blog and many downloads available as well.

Tovamesh.com: I like the layout but I do want more interaction with mine. I do like the are you a training leader? Department leader: emerging leader? Componenets because I am addressing Nurses, Nurse Leaders, Legal Nurse Consultants… this would be important to establish right up front. I particularly like the video enhanced special report the new prospect has access to. I will do this for my site. I think it is also cool that you can change the color of the landing page to your liking.

www.thebrindlecove.com: I like a lot of things on this website but it is a bit difficult to navigate for even me. I like the short one minute capture of audio cds. I do plan to have CD material available. I do like the what you get with each level of membership under brindlelink tab. Some of the pages are not easy to read because the color is too dark and the font color is not contrasted enough. I like the tips in ten downloads on CD as well. I can see this working with mine as similar formatting with of course difference content.

www.ginaforsby.org: I do like the section she has on photo gallery where I can post event that have taken place as I speak, and work one-on-one with nurses across the country. (not the fashion shoot ?).

www.7horizons.com: I love the rollover interaction, the eyes constantly moving to the movement across the site.
http://www.dorvesta.org/DorvestaMultimedia.aspx?VideoId=8830461729004&type=M Quick lane video using sketchpad is a cool idea.

www.pebblevault.com - nice and clean

11. Please give us a list of websites that you DON’T Like and Why you Don’t like them.

www.lurn.com: landing page is way too crowded, too many colors, I don’t know where to go for what I would be looking for. Font is too small with large amounts of content.

www.casewardhub.com: this site is way too busy and difficult to navigate however I do like the page titled: Memorable BRWP cases. I would use a page like this for memorable Caring Summit experiences that would encourage others and remember the great things nurses do.

www.wardskills.com: Do not like at all. Way to juvenile.

Colour Scheme:

The colors palette I like is…. I think you will get the general idea of the color scheme. I like the yellow on dark colors so it pops, make sense?

F7C40E
4819A9
2E1FAC
F7D80E
Updates

Payment is guaranteed for this project now! :)

Thank you

Target Market(s)

Customers: Nurses, Advanced Practice Nurses, Legal Nurse Consultants, Attorneys for the clinical/medical information, Universities that offer nursing

Values:
I – Integrity
A – Accountability

Industry/Entity Type

Healthcare

Requirements
Must have
• professional, clean, VERY HIGH QUALITY IMAGES/ PHOTOGRAPHY e.g. PixQuarry
Nice to have
• Brock:
I have shown the design template to several people to get their first impression. I was shocked. They thought of the Tacoma Riveters! The football team. Ouch. I don’t want that. Crazy what others see.
Can we please change the color scheme to incorporate the colors below with the same layout. The Layout is good, it is the color I need to work a bit more on. Sorry about this but I don’t want to be a Riveters fan.

336699
FFCC66
FFFFFF
003366

Yvonne

New logo required: Caring Summit - DO NOT USE MEDICAL
Should not have
• childish graphics, or icons.
Don't want to see unprofessional site with clumsy type or template type designs. We can include some photos.

```html
<!DOCTYPE html>
<html lang="de">
<head>
<meta charset="utf-8">
<title>Caring Summit</title>
<link href="https://fonts.googleapis.com/css2?family=Ubuntu:wght@400;500&family=Open+Sans:wght@400;600;700&display=swap" rel="stylesheet">
<style>
:root{
  --orange:#f59b1c;
  --orange-deep:#f39019;
  --band-top:#fdc62e;
  --band-bottom:#f8a21d;
  --ink:#3a3a3a;
  --ink-soft:#555;
  --line:#d9d9d9;
  --panel:#e9e9e9;
  --white:#fff;
}
*{box-sizing:border-box;margin:0;padding:0}
html,body{width:819px;height:1200px;overflow:hidden;background:var(--white)}
body{font-family:"Open Sans",sans-serif;color:var(--ink);position:relative}
.abs{position:absolute}
.top-bar{left:0;top:0;width:819px;height:7px;background:linear-gradient(var(--band-top),var(--orange))}
.social{left:543px;top:20px;display:flex;gap:6px}
.social span{width:11px;height:11px;border-radius:2px;display:block}
.rule{height:1px;background:var(--line)}
.logo{left:128px;top:43px;font-family:"Ubuntu",sans-serif;font-size:25px;color:var(--orange);letter-spacing:.5px}
.search{left:482px;top:82px;width:208px;height:22px;border:3px solid #e4e4e4;border-radius:3px;background:#fff;display:flex;align-items:center;font-size:6.5px}
.search .field{flex:1;padding-left:17px;color:#aaa;font-style:italic;position:relative}
.search svg{position:absolute;left:4px;top:-1px}
.search .go{width:38px;height:100%;border-left:1px solid #ddd;display:flex;align-items:center;justify-content:center;color:#444;font-size:7px;font-weight:600}
.nav{left:129px;top:116px;height:28px;display:flex;border:1px solid #ccc;border-radius:2px;background:linear-gradient(#fafafa,#e8e8e8)}
.nav a{display:flex;align-items:center;justify-content:center;font-size:7.5px;font-weight:700;color:#444;text-decoration:none;border-right:1px solid #d0d0d0}
.nav a:last-child{border-right:0}
.ph{display:block}
.hero-title{left:446px;top:171px;font-size:12.5px;color:#333}
.hero-text{left:446px;top:197px;width:222px;font-size:7.3px;line-height:11.7px;color:#444}
.btn{border:1px solid #ccc;background:linear-gradient(#fff,#f0f0f0);font-size:7.5px;color:#444;display:flex;align-items:center;justify-content:center}
.dots{left:396px;top:341px;display:flex;gap:3px}
.dots span{width:7px;height:7px;border-radius:50%;background:#555}
.dots span:first-child{background:var(--orange)}
.side{left:122px;top:362px;width:112px;height:191px;border:1px solid #ccc;padding:3px 0 0 8px;font-size:7.5px;line-height:11.7px;color:#333}
.main-title{left:241px;top:361px;font-family:"Ubuntu",sans-serif;font-size:11px;color:var(--orange)}
.main-text{left:241px;top:380px;width:430px;font-size:7.5px;line-height:12.8px;color:#444}
.main-text h4{font-weight:400;color:#222;margin-top:4px}
.login{left:534px;top:365px;width:164px;height:109px;background:var(--panel);border-radius:4px}
.login-tab{left:580px;top:362px;width:74px;height:24px;background:linear-gradient(#fbb534,var(--orange-deep));border-radius:0 0 4px 4px;color:#222;font-size:7.5px;display:flex;align-items:center;justify-content:center;gap:3px}
.input{left:552px;width:132px;height:18px;background:#fff;border:1px solid #ddd;border-radius:3px;font-size:7px;padding-left:5px;display:flex;align-items:center;color:#333}
.remember{left:553px;top:454px;font-size:6.5px;display:flex;align-items:center;gap:3px;color:#333}
.remember i{width:5px;height:5px;border-radius:50%;background:var(--orange);display:block}
.signin{left:632px;top:450px;width:52px;height:16px;border-radius:8px;background:linear-gradient(#fbb534,var(--orange-deep));font-size:7px;color:#333;display:flex;align-items:center;justify-content:center}
.video-head{left:122px;top:570px;font-family:"Ubuntu",sans-serif;font-size:14.5px;color:var(--orange)}
.band{left:0;top:594px;width:819px;height:588px;background:linear-gradient(var(--band-top),var(--band-bottom) 35%,var(--band-bottom))}
.thumb{top:609px;width:170px;height:110px;border:2px solid #fff;background:linear-gradient(135deg,#f2f2f2,#cfd6dc)}
.thumb .play{position:absolute;left:73px;top:30px;width:26px;height:26px;background:var(--orange)}
.thumb .play svg{position:absolute;left:8px;top:7px}
.thumb .cap{position:absolute;left:0;bottom:0;width:100%;height:29px;background:rgba(70,70,70,.72);color:#fff;font-size:7.2px;line-height:10.5px;padding:4px 0 0 4px}
.problems{left:122px;top:730px;width:568px;height:163px;background:#fff;border-radius:3px}
.problems h2{position:absolute;left:12px;top:6px;font-family:"Ubuntu",sans-serif;font-weight:400;font-size:14px;color:var(--orange)}
.col{top:35px;font-size:7.5px;line-height:11.7px;color:#333}
.card{background:#fff;border:1px solid #e3e3e3}
.card h3{position:absolute;left:9px;top:10px;font-family:"Ubuntu",sans-serif;font-weight:400;font-size:11px;color:#333}
.card .pic{position:absolute;left:9px;top:29px;width:121px;height:86px}
.card p{position:absolute;left:141px;top:36px;width:70px;font-family:"Ubuntu",sans-serif;font-size:9.6px;line-height:12.8px;color:#333}
.card .btn{position:absolute;left:141px;width:58px;height:15px}
.side-card h3{position:absolute;left:7px;font-family:"Ubuntu",sans-serif;font-weight:400;font-size:11px;color:#222}
.follow-grid{left:6px;top:19px;display:grid;grid-template-columns:repeat(3,38px);gap:2px 2px}
.follow-grid span{height:38px;display:block}
.see{left:6px;top:128px;width:61px;height:8px;background:var(--orange);font-size:5px;color:#333;display:flex;align-items:center;justify-content:center}
.footer{left:0;top:1189px;width:819px;text-align:center;font-size:6.3px;color:#444}
</style>
</head>
<body>
<div class="abs top-bar"></div>
<div class="abs social" aria-label="Social links">
  <span style="background:#3b5a9a"></span><span style="background:#c9232d"></span><span style="background:#35aee2"></span><span style="background:#3c9b3c"></span>
</div>
<div class="abs rule" style="left:117px;top:38px;width:585px"></div>
<div class="abs logo">CARING SUMMIT</div>

<div class="abs search">
  <div class="field"><svg width="9" height="9" viewBox="0 0 10 10"><circle cx="4" cy="4" r="3" fill="none" stroke="#555" stroke-width="1.4"/><line x1="6.2" y1="6.2" x2="9" y2="9" stroke="#555" stroke-width="1.6"/></svg>Search on NestGuide</div>
  <div class="go">Search</div>
</div>

<nav class="abs nav">
  <a style="width:49px">Home</a><a style="width:55px">Services</a><a style="width:57px">Portfolio</a><a style="width:56px">Freebies</a><a style="width:63px">Showcase</a><a style="width:58px">Our Blog</a><a style="width:58px">About us</a><a style="width:53px">Contact</a><a style="width:112px">By PixelHarbor.com</a>
</nav>

<div class="abs ph" role="img" aria-label="Smiling nurse in a surgical cap with a family in a hospital room behind her" style="left:158px;top:169px;width:264px;height:165px;background:linear-gradient(120deg,#7fa9d6,#cfd8e2 55%,#8b7f73)"></div>
<div class="abs hero-title">Gestational Diabetes</div>
<div class="abs hero-text">Overview of Gestational Diabetes Gestational diabetes is a mild diabetes that is first recognized in pregnancy. &nbsp;Taking control of it lessens the chance it will do any harm to the baby and once managed all is typically fine. &nbsp;It occurs because the mother’s pancreas does not make enough extra insulin to control the blood sugar, needed when hormones from the placenta…</div>
<div class="abs btn" style="left:608px;top:296px;width:58px;height:15px">read more..</div>
<div class="abs rule" style="left:117px;top:345px;width:585px"></div>
<div class="abs dots"><span></span><span></span><span></span></div>

<aside class="abs side">Geburt<br>Hebammen-Arbeit<br>Hebammen-Suche<br>Hebammen-<br>Studiengänge<br>Eltern &amp; Hebammen<br>Forum Externer Link<br>Linkliste<br>Hebammen-Gremium<br>Internationaler Ethik-<br>Kodex für Hebammen<br>Von A - Z<br>Fortbildungsveranstalt<br>ungen Externer Link<br>Informationen</aside>

<h1 class="abs main-title" style="font-weight:400">Geburt</h1>
<div class="abs main-text">
  <p style="width:280px">Wie kann ich mein Kind zur Welt bringen?<br>Es gibt verschiedenene Arten, ein Kind auf die Welt zu bringen.<br>Zu Hause<br>In Österreich kommen ca. 2% der Babys zu Hause auf die Welt. Bei einer Hausgeburt werden Sie vor, während und in den ersten Wochen nach der Geburt von "Ihrer" Hebamme betreut. Ein Arzt wird nur hinzugezogen, wenn Probleme auftreten.</p>
  <h4>In einem Krankenhaus</h4>
  <p>Die meisten Geburten finden derzeit in einem Krankenhaus mit geburtshilflicher Abteilung statt. Die betreuende Hebamme kann kann man sich dabei meistens nicht aussuchen (obwohl auch hier manchmal die Möglichkeit einer Wahlhebamme besteht), diese wird gemeinsam mit dem betreuenden Arzt vom Spital gestellt. Manche Spitäler bieten gewisse Zusatzleistungen, die die Geburt erleichtern sollen.</p>
</div>

<div class="abs login"></div>
<div class="abs login-tab"><svg width="8" height="9" viewBox="0 0 8 9"><path d="M2 4V2.6a2 2 0 0 1 4 0V4" fill="none" stroke="#222" stroke-width="1.2"/><rect x="1" y="4" width="6" height="5" fill="#222"/></svg>Login Now</div>
<div class="abs input" style="top:400px">Username</div>
<div class="abs input" style="top:426px">•••••••••</div>
<div class="abs remember"><i></i>Remember Me</div>
<div class="abs signin">Sign-in</div>

<div class="abs video-head">Vedio that help you to know more about your profetion</div>
<div class="abs band"></div>

<div class="abs thumb" style="left:133px" role="img" aria-label="Video still: doctor with clipboard in a clinic"><div class="play"><svg width="10" height="12"><path d="M0 0L10 6L0 12Z" fill="#fff"/></svg></div><div class="cap">what kind of problem mother face<br>during pregnency period ?</div></div>
<div class="abs thumb" style="left:325px" role="img" aria-label="Video still: doctor with clipboard in a clinic"><div class="play"><svg width="10" height="12"><path d="M0 0L10 6L0 12Z" fill="#fff"/></svg></div><div class="cap">what kind of problem mother face<br>during pregnency period ?</div></div>
<div class="abs thumb" style="left:518px" role="img" aria-label="Video still: doctor with clipboard in a clinic"><div class="play"><svg width="10" height="12"><path d="M0 0L10 6L0 12Z" fill="#fff"/></svg></div><div class="cap">what kind of problem mother face<br>during pregnency period ?</div></div>

<section class="abs problems">
  <h2>We treand people in different problem :</h2>
  <div class="abs col" style="left:14px">Eltern &amp; Hebammen<br>Forum Externer Link<br>Linkliste<br>Hebammen-Gremium<br>Internationaler Ethik-<br>Kodex für Hebammen<br>Von A - Z<br>Fortbildungsveranstalt<br>ungen Externer Link<br>Informationen</div>
  <div class="abs col" style="left:128px">Eltern &amp; Hebammen<br>Forum Externer Link<br>Linkliste<br>Hebammen-Gremium<br>Internationaler Ethik-<br>Kodex für Hebammen<br>Von A - Z<br>Fortbildungsveranstalt<br>ungen Externer Link<br>Informationen</div>
  <div class="abs col" style="left:242px">Eltern &amp; Hebammen<br>Forum Externer Link<br>Linkliste<br>Hebammen-Gremium<br>Internationaler Ethik-<br>Kodex für Hebammen<br>Von A - Z<br>Fortbildungsveranstalt<br>ungen Externer Link<br>Informationen</div>
  <div class="abs col" style="left:362px">Eltern &amp; Hebammen<br>Forum Externer Link<br>Linkliste<br>Hebammen-Gremium<br>Internationaler Ethik-<br>Kodex für Hebammen<br>Von A - Z<br>Fortbildungsveranstalt<br>ungen Externer Link<br>Informationen</div>
  <div class="abs col" style="left:470px">Eltern &amp; Hebammen<br>Forum Externer Link<br>Linkliste<br>Hebammen-Gremium<br>Internationaler Ethik-<br>Kodex für Hebammen<br>Von A - Z<br>Fortbildungsveranstalt<br>ungen Externer Link<br>Informationen</div>
</section>

<article class="abs card" style="left:122px;top:904px;width:212px;height:128px">
  <h3>WHAT U SHOULD DO !</h3>
  <div class="pic" role="img" aria-label="Mother holding her newborn baby" style="background:linear-gradient(120deg,#d9b8a0,#f3e6dc 55%,#c9566a)"></div>
  <p>My post-partum belly made a stranger ask me when I was due!</p>
  <div class="btn" style="top:100px">read more..</div>
</article>
<article class="abs card" style="left:342px;top:904px;width:211px;height:128px">
  <h3>GIVE CUSTOMER HEALTHY FOOD</h3>
  <div class="pic" role="img" aria-label="Pregnant woman carrying a basket of fresh vegetables" style="background:linear-gradient(160deg,#f3f3f3,#8fb4c6 45%,#7aa03a 75%,#c94a2c)"></div>
  <p>Healthy food will take care of my baby health.</p>
  <div class="btn" style="top:100px">read more..</div>
</article>
<article class="abs card side-card" style="left:561px;top:904px;width:137px;height:115px">
  <h3 style="top:6px">Featured Video</h3>
  <div class="abs" style="left:7px;top:22px;font-size:7.5px;color:#444">Inside pregnancy: Labor and birth</div>
  <div class="abs" role="img" aria-label="Video still of a newborn baby" style="left:18px;top:35px;width:91px;height:65px;background:linear-gradient(135deg,#efe2d6,#d9b9a4)"></div>
  <svg class="abs" style="left:56px;top:59px" width="16" height="16" viewBox="0 0 16 16"><circle cx="8" cy="8" r="7.5" fill="rgba(255,255,255,.55)"/><path d="M6 4.5L11.5 8L6 11.5Z" fill="#fff"/></svg>
</article>

<article class="abs card" style="left:122px;top:1040px;width:212px;height:130px">
  <h3>WHAT U DO IN CLIEND LABOR PAIN</h3>
  <div class="pic" role="img" aria-label="Mother resting in a hospital bed during labor" style="background:linear-gradient(150deg,#6e5b52,#c7c0ba 50%,#e6e1dc)"></div>
  <p>I don't want family hanging at the hospital when I'm in labor.</p>
  <div class="btn" style="top:100px">read more..</div>
</article>
<article class="abs card" style="left:342px;top:1040px;width:211px;height:130px">
  <h3>HELP PEOPLE FAMILY PLANNING</h3>
  <div class="pic" role="img" aria-label="Happy young couple smiling together" style="background:linear-gradient(120deg,#c28a66,#e3b896 50%,#6b4a36)"></div>
  <p>My mother-in-law doesn't want my hus-band to get the Big V!</p>
  <div class="btn" style="top:100px">read more..</div>
</article>
<article class="abs card side-card" style="left:561px;top:1028px;width:137px;height:142px">
  <h3 style="top:3px">Follow Us</h3>
  <div class="abs follow-grid" role="img" aria-label="Grid of six baby photos shared by followers">
    <span style="background:#9fc3a0"></span><span style="background:#e7b8c4"></span><span style="background:#eadbd0"></span>
    <span style="background:#a9c4d8"></span><span style="background:#d7b8a8"></span><span style="background:#d9c2b4"></span>
  </div>
  <div class="abs see">See &amp; add photo</div>
</article>

<div class="abs footer">© Copyright 2012 LHV - Alle Rechte vorbehalten - Impressum - Sitemap - TOP</div>
</body>
</html>
```